Water Filter Company Needs Bizz Cards!!

Need business cards for my company. We sell whole home water filters and salt free water softeners. No more buying bottled water. Our filtering units filter out all heavy metals, chlorine, and VOC's, last 15 years, and are maintenance free and supply your whole home with spring quality alkaline water. Our Salt free water conditioners, eliminate hard water and scale, without lowering the ph, or TDS's (total Dissolved solids)

I think this is the color code we are using on my site. My logo looks good behind it. #192841

Website will be www.Brovexa.com

Industry/Entity Type

Water Purification

Contact Information for Business Card

For now, just insert standard Dummy text. I need these text lines for the info to be editable so i can make them for multiple employees. I do have Photoshop and illustrator, unless there is a simpler program i can use solely for biz cards

Font styles to use
Sans Serif

Requirements
Must have
• Use my preexisting logo.

www.BroVexa.com

Spring Quality Alkaline Water at every tap.

List out services. Whole Home Water Filters, Salt Free Water Softeners, Clarimont KT7, UV Sterilizers
Nice to have
• I think this is the color code we are using on my site. My logo looks good behind it. #192841 or black. Please no white or light blue backgrounds.

Maybe a picture of my tank.

Slogan like Spring Quality Alkaline Water at every tap.
And just list the services Whole Home Water Filters, Salt Free Water Softeners, Clarimont KT7, UV Sterilizers

I think I would like to not have a contrasting textured logo like I see on some of them. I may use it for my personal cards, but new employees may not want the extra expense.
Should not have
• A different logo than the one provided.

White or baby blue backgrounds. Use the color code, or blacks.

```html
<!DOCTYPE html>
<html lang="en">
<head>
<meta charset="UTF-8">
<title>Brovexa Business Cards</title>
<link rel="stylesheet" href="https://fonts.googleapis.com/css2?family=Open+Sans:wght@400;600;700;800&display=swap">
<style>
  :root {
    --navy: #192841;
    --navy-deep: #131f34;
    --navy-soft: #24344f;
    --aqua: #2aa3dc;
    --aqua-light: #45b6ea;
    --silver: #c9ccd1;
    --white: #ffffff;
    --stage: #d9d9d7;
  }
  * { box-sizing: border-box; margin: 0; padding: 0; }
  html, body {
    width: 1200px; height: 675px; overflow: hidden;
    background: var(--stage);
    font-family: "Open Sans", Arial, sans-serif;
  }
  .stage {
    position: relative; width: 1200px; height: 675px;
    display: flex; align-items: center; justify-content: center; gap: 60px;
  }
  .card {
    position: relative; width: 520px; height: 297px;
    border-radius: 14px; overflow: hidden;
    background: linear-gradient(160deg, var(--navy-soft) 0%, var(--navy) 45%, var(--navy-deep) 100%);
    box-shadow: 0 6px 18px rgba(0,0,0,0.18);
  }
  .brand {
    display: flex; align-items: center; gap: 10px;
  }
  .brand-dot {
    width: 26px; height: 26px; border-radius: 50%;
    background: var(--aqua-light);
  }
  .brand-name {
    font-weight: 800; font-size: 40px; letter-spacing: -0.5px;
    color: var(--aqua-light); line-height: 1;
  }

  /* Front: contact side */
  .card-front .brand { position: absolute; left: 34px; top: 30px; }
  .card-front .wave { position: absolute; inset: 0; }
  .holder {
    position: absolute; right: 48px; top: 118px; text-align: right;
  }
  .holder-name {
    font-weight: 700; font-size: 27px; letter-spacing: 1px;
    color: var(--aqua-light); line-height: 1.1;
  }
  .holder-role { font-size: 12px; color: var(--white); }
  .contact {
    position: absolute; left: 30px; top: 178px;
    list-style: none; color: var(--white); font-size: 13px; line-height: 1.35;
  }
  .contact li { display: flex; align-items: flex-start; gap: 10px; margin-bottom: 2px; }
  .contact svg { flex: none; margin-top: 2px; }
  .website {
    position: absolute; right: 30px; bottom: 12px;
    display: flex; align-items: center; gap: 8px;
    color: var(--white); font-size: 14px; font-weight: 600;
  }

  /* Back: services side */
  .card-back {
    display: flex; flex-direction: column; align-items: center; justify-content: center;
    gap: 10px; text-align: center;
  }
  .card-back .brand { margin-bottom: 14px; }
  .card-back .brand-name { font-size: 46px; }
  .services { color: var(--white); font-size: 14px; line-height: 1.5; }
  .services-row { display: flex; gap: 14px; justify-content: center; }
  .services-row span::before { content: "\2022"; margin-right: 6px; }
  .services-tag {
    display: inline-block; background: var(--aqua);
    color: var(--white); font-size: 12px; font-weight: 600;
    padding: 1px 8px; border-radius: 2px; margin: 3px 0;
  }
  .slogan {
    color: var(--aqua-light); font-weight: 700; font-size: 14px; margin-top: 6px;
  }
</style>
</head>
<body>
<main class="stage">

  <section class="card card-front" aria-label="Business card, contact side">
    <svg class="wave" width="520" height="297" viewBox="0 0 520 297" aria-hidden="true">
      <path d="M0,150 C120,125 220,165 320,215 S460,262 520,258 L520,297 L0,297 Z" fill="var(--aqua)"/>
      <path d="M0,140 C120,112 225,150 325,200 S465,250 520,246" fill="none" stroke="var(--silver)" stroke-width="9"/>
      <path d="M0,130 C120,104 225,140 325,190 S465,238 520,236" fill="none" stroke="var(--silver)" stroke-width="2" opacity="0.6"/>
    </svg>

    <div class="brand">
      <span class="brand-dot"></span>
      <span class="brand-name">Brovexa</span>
    </div>

    <div class="holder">
      <p class="holder-name">NAME</p>
      <p class="holder-role">Designation</p>
    </div>

    <ul class="contact">
      <li>
        <svg width="12" height="14" viewBox="0 0 12 14"><path d="M6 0a5 5 0 0 0-5 5c0 4 5 9 5 9s5-5 5-9a5 5 0 0 0-5-5zm0 7a2 2 0 1 1 0-4 2 2 0 0 1 0 4z" fill="var(--white)"/></svg>
        <span>42 Linden Crest Road,<br>Maple Hollow</span>
      </li>
      <li>
        <svg width="12" height="12" viewBox="0 0 12 12"><path d="M2.5 0.5l2 2.5-1.2 1.4a7 7 0 0 0 4.3 4.3L9 7.5l2.5 2-1.3 2A9.5 9.5 0 0 1 0.5 1.8z" fill="var(--white)"/></svg>
        <span>55 0100 482 317</span>
      </li>
      <li>
        <svg width="12" height="12" viewBox="0 0 12 12"><rect x="0.5" y="2" width="11" height="8" rx="1" fill="none" stroke="var(--white)"/><path d="M0.5 2.5L6 7l5.5-4.5" fill="none" stroke="var(--white)"/></svg>
        <span>hello@brovexa.co</span>
      </li>
    </ul>

    <div class="website">
      <svg width="13" height="13" viewBox="0 0 14 14"><circle cx="7" cy="7" r="6" fill="none" stroke="var(--white)" stroke-width="1.2"/><ellipse cx="7" cy="7" rx="2.6" ry="6" fill="none" stroke="var(--white)" stroke-width="1"/><path d="M1 7h12" stroke="var(--white)" stroke-width="1"/></svg>
      <span>www.Brovexa.com</span>
    </div>
  </section>

  <section class="card card-back" aria-label="Business card, services side">
    <div class="brand">
      <span class="brand-dot"></span>
      <span class="brand-name">Brovexa</span>
    </div>
    <div class="services">
      <div class="services-row"><span>Whole Home Water Filters</span><span>Salt Free Water Softeners</span></div>
      <span class="services-tag">Services</span>
      <div class="services-row"><span>Clarimont KT7</span><span>UV Sterilizers</span></div>
    </div>
    <p class="slogan">Spring Quality Alkaline Water At Every Tap.</p>
  </section>

</main>
</body>
</html>
```